Handyman Business Card and website logo design

I need a logo for my new handyman business. The logo will be used for my website, business cards, and Facebook pages. I want my business card to have this logo and have a simplistic and nicely flowing design with a handyman feel.

The name of my business is KT Nest Fixer. (Dr is for doctor NOT Drive). So my thoughts for my logo is a handyman with a stethoscope and looking like a doctor examining a house. With handyman will have a tool-belt on and holding a drill or some other well recognized tool. Basically a handyman doctor examining someones "precious home" so that he can prescribe the right "fix" for them.

Martin Pellworth (CEO)
KTNestFixer
4137 Wyndmoor Court
Naperville, IL 60391

```html
<!DOCTYPE html>
<html lang="en">
<head>
<meta charset="utf-8">
<title>KT Nest Fixer – Business Card</title>
<link rel="stylesheet" href="https://fonts.googleapis.com/css2?family=Barlow:wght@400;700&display=swap">
<style>
  :root {
    --bg: #ffffff;
    --brown-dark: #6b5335;
    --tan: #b08a4a;
    --cream: #d6bb92;
    --white: #ffffff;
    --label: #b3b3b3;
  }
  * { margin: 0; padding: 0; box-sizing: border-box; }
  html, body {
    width: 1200px; height: 1000px; overflow: hidden;
    background: var(--bg);
    font-family: "Barlow", Arial, sans-serif;
  }
  .canvas { position: relative; width: 1200px; height: 1000px; }

  .card {
    position: absolute; top: 57px; width: 487px; height: 856px;
    background: var(--brown-dark); overflow: hidden;
  }
  .card--front { left: 88px; }
  .card--reverse { left: 624px; }

  .card__brand-area { position: absolute; left: 0; top: 0; width: 100%; height: 453px; }
  .brand-mark {
    position: absolute; left: 168px; top: 150px;
    width: 150px; height: 150px; border-radius: 50%;
    background: var(--cream);
  }
  .wordmark {
    position: absolute; left: 72px; top: 290px;
    color: var(--white); font-weight: 700;
    font-size: 68px; line-height: 64px; letter-spacing: 0.5px;
    text-transform: uppercase;
  }

  .card__info {
    position: absolute; left: 0; top: 453px; width: 100%; height: 365px;
    background: var(--tan); color: var(--white);
    padding: 43px 0 0 72px;
  }

  .contact__name { font-weight: 700; font-size: 22px; line-height: 30px; margin-bottom: 11px; }
  .contact__role { font-size: 17px; letter-spacing: 0.5px; }
  .contact__line { font-size: 24px; line-height: 33px; }
  .contact__group { margin-bottom: 12px; }
  .contact__group--tight { margin-bottom: 14px; }

  .services__intro { font-size: 24px; line-height: 33px; margin-bottom: 12px; }
  .services__cols { display: flex; }
  .services__list { list-style: none; font-size: 24px; line-height: 33px; }
  .services__list:first-child { width: 189px; }
  .services__list li::before {
    content: ""; display: inline-block; width: 6px; height: 6px;
    border-radius: 50%; background: var(--cream);
    margin: 0 6px 5px 0; vertical-align: middle;
  }

  .side-label {
    position: absolute; top: 948px; width: 487px; text-align: center;
    color: var(--label); font-size: 18px; letter-spacing: 2.5px;
  }
  .side-label--front { left: 88px; }
  .side-label--reverse { left: 624px; }
</style>
</head>
<body>
<main class="canvas">

  <section class="card card--front" aria-label="Business card front">
    <div class="card__brand-area">
      <span class="brand-mark" aria-hidden="true"></span>
      <div class="wordmark">KT Nest<br>Fixer</div>
    </div>
    <div class="card__info">
      <p class="contact__name">Martin Pellworth <span class="contact__role">(CEO)</span></p>
      <div class="contact__group">
        <p class="contact__line">KT Nest Fixer</p>
        <p class="contact__line">4137 Wyndmoor Court</p>
        <p class="contact__line">Naperville, IL 60391</p>
      </div>
      <p class="contact__line contact__group--tight">Call: (123) 555-0147</p>
      <p class="contact__line contact__group--tight">Email: mp@ktnestfixer.com</p>
      <p class="contact__line">Web: www.ktnestfixer.com</p>
    </div>
  </section>

  <section class="card card--reverse" aria-label="Business card reverse">
    <div class="card__brand-area">
      <span class="brand-mark" aria-hidden="true"></span>
      <div class="wordmark">KT Nest<br>Fixer</div>
    </div>
    <div class="card__info">
      <p class="services__intro">All domestic and household<br>projects considered including:</p>
      <div class="services__cols">
        <ul class="services__list">
          <li>Roof repairs</li>
          <li>Guttering</li>
          <li>Decorating</li>
          <li>Flooring</li>
          <li>Plumbing</li>
          <li>Electrical</li>
        </ul>
        <ul class="services__list">
          <li>Gardening</li>
          <li>Roof repairs</li>
          <li>Maintenance</li>
          <li>Joinery</li>
          <li>Stone work</li>
        </ul>
      </div>
    </div>
  </section>

  <p class="side-label side-label--front">FRONT</p>
  <p class="side-label side-label--reverse">REVERSE</p>

</main>
</body>
</html>
```